Political themed graphic for contemporary church sermon series

Contemporary church in California need a graphic design for a sermon series. The sermon series will be focused on the upcoming presidential election. The sermon series is titled for the question "who will be the next president":

Title: 45
Subtitle: Who will it be / Does it matter

The design should use red, white and blue and should possibly have the cedar hall in the graphic somewhere. Maybe like a watermark or something to that effect.

Target Market(s)

Contemporary design,

Industry/Entity Type

Church

Font styles to use
Serif
Sans Serif

Colors
0555a3
ec1f27
ffffff

Requirements
Must have
• Political theme, red, white and blue (contemporary color palette). Cedar hall screened back in the design somewhere.
• the title large: 45
• and subtitle: Who will it be | Does it matter
Should not have
• I'm not looking for cheesy graphics with elephant and a donkey.

```html
<!DOCTYPE html>
<html lang="en">
<head>
<meta charset="utf-8">
<title>45 – Sermon Series</title>
<link href="https://fonts.googleapis.com/css2?family=Bitter:wght@800&family=Exo+2:ital,wght@1,900&family=Jost:wght@500;600&display=swap" rel="stylesheet">
<style>
  :root {
    --blue: #0555a3;
    --blue-light: #2a8fd6;
    --red: #ec1f27;
    --red-deep: #b5121b;
    --white: #ffffff;
    --card-top: #f7f7f8;
    --card-bottom: #e6e7e9;
    --page: #dcdde0;
  }
  * { box-sizing: border-box; margin: 0; padding: 0; }
  html, body { width: 1200px; height: 1200px; overflow: hidden; background: var(--page); }
  .series-card {
    position: absolute; left: 0; top: 263px;
    width: 1200px; height: 674px; overflow: hidden;
    background: linear-gradient(180deg, var(--card-top), var(--card-bottom));
  }
  .series-number {
    position: absolute; left: 80px; top: 66px;
    font: italic 900 170px/1 "Exo 2", sans-serif;
    color: var(--white);
    -webkit-text-stroke: 5px var(--red);
    letter-spacing: 4px;
  }
  .building {
    position: absolute; left: 420px; top: 48px; width: 354px; height: 164px;
    background: linear-gradient(180deg, var(--blue-light), var(--blue));
  }
  .building-shadow {
    position: absolute; left: 450px; top: 240px; width: 300px; height: 18px;
    border-radius: 50%;
    background: radial-gradient(ellipse, rgba(0,0,0,.28), rgba(0,0,0,0) 70%);
  }
  .year {
    position: absolute; left: 846px; top: 78px;
    font: 600 96px/1 "Jost", sans-serif; color: var(--red-deep); letter-spacing: -2px;
  }
  .matchup {
    position: absolute; left: 850px; top: 178px;
    font: 600 14px/1 "Jost", sans-serif; color: var(--blue);
  }
  .ribbons {
    position: absolute; left: 840px; top: 236px; width: 360px; height: 438px;
    background: linear-gradient(135deg, var(--blue) 0%, var(--blue-light) 30%, var(--red-deep) 55%, var(--blue) 85%);
  }
  .rule { position: absolute; top: 282px; width: 8px; height: 372px; }
  .rule--blue { left: 106px; background: linear-gradient(180deg, var(--blue-light), var(--blue)); }
  .rule--red { left: 130px; background: linear-gradient(180deg, var(--red-deep), var(--red), var(--red-deep)); }
  .subtitle {
    position: absolute; left: 178px;
    font: 800 88px/1 "Bitter", serif; letter-spacing: -0.5px; white-space: nowrap;
  }
  .subtitle--who { top: 320px; color: var(--blue); }
  .subtitle--matter { top: 424px; color: var(--red-deep); }
  .election-label {
    position: absolute; left: 184px; top: 566px;
    font: 500 30px/1.05 "Jost", sans-serif; color: var(--blue-light);
  }
  .election-label strong { display: block; font-size: 43px; font-weight: 500; color: var(--blue); }
</style>
</head>
<body>
  <main class="series-card">
    <div class="series-number">45</div>

    <div class="ribbons" role="img" aria-label="Flowing red, white and blue flag ribbons with stars"></div>

    <div class="building-shadow"></div>
    <div class="building" role="img" aria-label="Cedar hall building illustration"></div>

    <div class="year">2016</div>
    <div class="matchup">DEMOCRATS VS REPUBLICANS</div>

    <span class="rule rule--blue"></span>
    <span class="rule rule--red"></span>

    <h1 class="subtitle subtitle--who">Who will it be ?</h1>
    <h2 class="subtitle subtitle--matter">Does it matter?</h2>

    <p class="election-label">PRESIDENTIAL <strong>ELECTION</strong></p>
  </main>
</body>
</html>
```